Bref créative
Business Cards and Letterhead
85 mm x 55 mm / DIN A4 210 mm × 297 mm
Professional
Dominik R. Hartl
Lindenweg 7, 14471 Potsdam
info@lbr-planung.example
www.lbr-planung.example
Please use the standard german sizes for business cards and letters:
85 mm x 55 mm
DIN A4: 210 mm × 297 mm

```html
<!DOCTYPE html>
<html lang="de">
<head>
<meta charset="utf-8">
<title>lbrplanung – Visitenkarten</title>
<link rel="stylesheet" href="https://fonts.googleapis.com/css2?family=Roboto+Condensed:wght@400;700&display=swap">
<style>
  :root {
    --stage: #2b2b2b;
    --card-white: #ffffff;
    --card-black: #0d0d0d;
    --orange: #f28c1c;
    --ink: #262626;
    --ink-soft: #555555;
    --grey-band: #3a3a3a;
  }
  * { margin: 0; padding: 0; box-sizing: border-box; }
  html, body { width: 1200px; height: 718px; overflow: hidden; }
  body {
    background: var(--stage);
    font-family: "Roboto Condensed", Arial, sans-serif;
    color: var(--ink);
    position: relative;
  }
  .card { position: absolute; overflow: hidden; box-shadow: 0 4px 14px rgba(0,0,0,.45); }
  .card-back { left: 403px; top: 67px; width: 377px; height: 269px; background: var(--card-black); }
  .card-front { top: 305px; width: 386px; height: 283px; background: var(--card-white); }
  .card-front--left { left: 209px; }
  .card-front--right { left: 605px; }
  .card-art { position: absolute; inset: 0; width: 100%; height: 100%; }

  .wordmark {
    position: absolute; display: flex; align-items: center; gap: 7px;
    font-weight: 700; letter-spacing: .3px; white-space: nowrap; line-height: 1;
  }
  .wordmark__square { width: 12px; height: 12px; background: var(--orange); }
  .card-back .wordmark { left: 50%; top: 50%; transform: translate(-50%, -50%); font-size: 34px; color: #ffffff; }
  .card-back .wordmark__square { width: 18px; height: 18px; }
  .card-front .wordmark { font-size: 25px; color: var(--ink); }
  .card-front--left .wordmark { left: 18px; top: 42px; }
  .card-front--right .wordmark { right: 16px; top: 100px; }

  .person-name { position: absolute; font-size: 18px; font-weight: 400; color: var(--ink); white-space: nowrap; }
  .card-front--left .person-name { left: 222px; top: 24px; }
  .card-front--right .person-name { left: 22px; top: 24px; }

  .contact { position: absolute; font-size: 9px; color: var(--ink-soft); white-space: nowrap; }
  .card-front--left .contact { left: 222px; top: 70px; }
  .card-front--right .contact { left: 22px; top: 70px; }
  .contact__address { color: var(--ink); font-size: 10px; margin-bottom: 8px; }
  .contact__body { position: relative; padding-left: 16px; }
  .contact__tag {
    position: absolute; left: 0; top: 50%;
    writing-mode: vertical-rl; transform: translateY(-50%) rotate(180deg);
    color: var(--orange); font-weight: 700; font-size: 9px; letter-spacing: 1px;
  }
  .contact__list { list-style: none; }
  .contact__list li { display: flex; align-items: center; gap: 4px; line-height: 14px; }
  .contact__dot { width: 6px; height: 6px; background: var(--orange); border-radius: 50%; flex: none; }
  .contact__label { color: var(--orange); width: 24px; flex: none; }
</style>
</head>
<body>

<section class="card card-back" aria-label="Visitenkarte Rückseite">
  <svg class="card-art" viewBox="0 0 377 269" aria-hidden="true">
    <polygon points="0,40 100,40 116,56 0,56" fill="var(--orange)"/>
    <polygon points="0,64 62,64 76,78 0,78" fill="var(--grey-band)"/>
  </svg>
  <div class="wordmark"><span class="wordmark__square"></span>lbrplanung</div>
</section>

<section class="card card-front card-front--left" aria-label="Visitenkarte Vorderseite">
  <svg class="card-art" viewBox="0 0 386 283" aria-hidden="true">
    <polygon points="0,220 122,220 129,230 0,230" fill="var(--orange)"/>
    <polygon points="0,230 129,230 165,283 0,283" fill="var(--card-black)"/>
  </svg>
  <div class="wordmark"><span class="wordmark__square"></span>lbrplanung</div>
  <h1 class="person-name">Dominik R. Hartl</h1>
  <div class="contact">
    <p class="contact__address">Lindenweg 7, 14471 Potsdam</p>
    <div class="contact__body">
      <span class="contact__tag">Kontakt</span>
      <ul class="contact__list">
        <li><span class="contact__dot"></span><span class="contact__label">Tel</span>(0331) 580 21 46-0</li>
        <li><span class="contact__dot"></span><span class="contact__label">Mobil</span>(0176) 552 03 81</li>
        <li><span class="contact__dot"></span><span class="contact__label">Fax</span>(0331) 580 21 46-9</li>
        <li><span class="contact__dot"></span><span class="contact__label">Mail</span>info@lbr-planung.example</li>
        <li><span class="contact__dot"></span><span class="contact__label">Web</span>www.lbr-planung.example</li>
      </ul>
    </div>
  </div>
</section>

<section class="card card-front card-front--right" aria-label="Visitenkarte Vorderseite Variante">
  <svg class="card-art" viewBox="0 0 386 283" aria-hidden="true">
    <polygon points="386,220 264,220 257,230 386,230" fill="var(--orange)"/>
    <polygon points="386,230 257,230 221,283 386,283" fill="var(--card-black)"/>
  </svg>
  <h1 class="person-name">Dominik R. Hartl</h1>
  <div class="contact">
    <p class="contact__address">Lindenweg 7, 14471 Potsdam</p>
    <div class="contact__body">
      <span class="contact__tag">Kontakt</span>
      <ul class="contact__list">
        <li><span class="contact__dot"></span><span class="contact__label">Tel</span>(0331) 580 21 46-0</li>
        <li><span class="contact__dot"></span><span class="contact__label">Mobil</span>(0176) 552 03 81</li>
        <li><span class="contact__dot"></span><span class="contact__label">Fax</span>(0331) 580 21 46-9</li>
        <li><span class="contact__dot"></span><span class="contact__label">Mail</span>info@lbr-planung.example</li>
        <li><span class="contact__dot"></span><span class="contact__label">Web</span>www.lbr-planung.example</li>
      </ul>
    </div>
  </div>
  <div class="wordmark"><span class="wordmark__square"></span>lbrplanung</div>
</section>

</body>
</html>
```